Square graphic for social media post

I want to create a 1080 x 1080px all-black image for the quote below that I can share on social media. I want the emphasis to be primarily on the quote, secondarily on the portrait, and third (smallest) on the logo. I want the background on the portrait to be edited so it's transparent and just shows the face of the person on a black background (no brick wall visible).

Graphic color: black
Text color: white
Content: "What we went through is going to make the greatest generation of hoteliers our industry has ever seen." << biggest text
Dorian Welk << smaller text
President, Marrowgate Hotels << smaller text
[image of person - use whichever version looks better to you]
[Add Lodging Ledger logo - whichever looks better to you]

This image needs to be readable when sized down much smaller (400x400?) so want the text and portrait to take up most of the space.

I'd like the output both as PNG and original file (preferably Canva). Thanks!

Target Market(s)

Hotel managers

Industry/Entity Type

Hospitality

Font styles to use
Sans Serif

Colors

Designer to choose colors to be used in the design.

Requirements
Must have
• Needs to focus on the quote and the person quoted (the portrait)

```html
<!DOCTYPE html>
<html lang="en">
<head>
<meta charset="utf-8">
<title>Quote card – Dorian Welk</title>
<link rel="stylesheet" href="https://fonts.googleapis.com/css2?family=Arimo:wght@400;700&display=swap">
<style>
  :root {
    --bg: #000000;
    --panel: #262626;
    --panel-edge: #3a3a3a;
    --gold: #d4a915;
    --text: #ffffff;
    --muted: #e6e6e6;
    --portrait-a: #c9c9c9;
    --portrait-b: #6d6f78;
  }
  * { margin: 0; padding: 0; box-sizing: border-box; }
  html, body {
    width: 1200px; height: 1200px; overflow: hidden;
    background: var(--bg);
  }
  .card {
    position: relative; width: 1200px; height: 1200px;
    background: var(--bg); overflow: hidden;
    font-family: "Arimo", Arial, sans-serif;
  }
  .card__shapes { position: absolute; inset: 0; width: 1200px; height: 1200px; }
  .quote-mark {
    position: absolute; color: var(--text);
    font-weight: 700; font-size: 230px; line-height: 1;
    letter-spacing: -18px;
    transform: scaleX(0.8);
  }
  .quote-mark--open { left: 6px; top: 32px; transform-origin: left top; }
  .quote {
    position: absolute; left: 102px; top: 112px; width: 960px;
    color: var(--text); font-weight: 700;
    font-size: 83px; line-height: 89px; letter-spacing: -0.5px;
  }
  .quote-mark--close {
    position: relative; display: inline-block;
    font-size: 230px; line-height: 0; vertical-align: -150px;
    margin-left: 4px; transform-origin: left center;
  }
  .portrait {
    position: absolute; left: 822px; top: 800px;
    width: 268px; height: 268px; border-radius: 50%;
    border: 4px solid #f2f2f2;
    background: radial-gradient(circle at 50% 38%, var(--portrait-a) 0%, #a9a9ad 45%, var(--portrait-b) 100%);
  }
  .attribution {
    position: absolute; left: 722px; top: 1080px; width: 468px;
    text-align: center; color: var(--text);
  }
  .attribution__name { font-size: 33px; font-weight: 400; letter-spacing: 1.5px; line-height: 40px; }
  .attribution__role { font-size: 26px; color: var(--muted); line-height: 34px; margin-top: 4px; }
  .brand {
    position: absolute; left: 40px; top: 1085px; width: 300px;
    text-align: center; color: var(--text);
    font-size: 30px; font-weight: 400; letter-spacing: 6px; line-height: 36px;
  }
</style>
</head>
<body>
<div class="card">
  <svg class="card__shapes" viewBox="0 0 1080 1080" aria-hidden="true">
    <defs>
      <linearGradient id="goldFade" x1="0" y1="0" x2="0" y2="1">
        <stop offset="0" stop-color="#d4a915"/>
        <stop offset="0.55" stop-color="#c99d12"/>
        <stop offset="1" stop-color="#8a6a08"/>
      </linearGradient>
      <linearGradient id="edgeFade" x1="0" y1="0" x2="0" y2="1">
        <stop offset="0" stop-color="#4a4a4a"/>
        <stop offset="1" stop-color="#1f1f1f"/>
      </linearGradient>
    </defs>
    <path d="M718 0 L1006 600 Q1016 624 994 640 L340 1010" fill="none" stroke="url(#goldFade)" stroke-width="5"/>
    <path d="M0 0 L688 0 L990 614 Q1002 645 975 660 L330 1000 L0 1000 Z" fill="var(--panel)"/>
    <rect x="0" y="0" width="9" height="980" fill="url(#edgeFade)"/>
    <ellipse cx="165" cy="1030" rx="170" ry="112" fill="var(--bg)"/>
  </svg>

  <div class="quote-mark quote-mark--open">“</div>
  <p class="quote">What we went<br>through is going<br>to make the<br>greatest<br>generation of<br>hoteliers our industry<br>has ever seen.<span class="quote-mark quote-mark--close">”</span></p>

  <div class="portrait" role="img" aria-label="Head-and-shoulders portrait of Dorian Welk on a light grey background"></div>

  <div class="attribution">
    <p class="attribution__name">DORIAN WELK</p>
    <p class="attribution__role">President, Marrowgate Hotels</p>
  </div>

  <p class="brand">LODGING<br>LEDGER</p>
</div>
</body>
</html>
```